Redesign of 2 real estate websites!

We need a redesign of our two real estate websites. These websites offer detailed information on the two real estates and need a modern fresh up.
Both websites should have the same design type, so you can see that they belong together, yet they should be in different colors. There is no logo to these pages, so the headlines can be integreated into the designs.
http://www.kolbrand-villa.de
http://www.leopold-kolbrand-haus.de/

```html
<!DOCTYPE html>
<html lang="de">
<head>
<meta charset="utf-8">
<title>Leopold-Kolbrand-Haus</title>
<link rel="stylesheet" href="https://fonts.googleapis.com/css2?family=Questrial&family=Open+Sans:wght@400;600&family=Montserrat:wght@700&family=Fjalla+One&display=swap">
<style>
:root{
  --orange:#e8601c;
  --orange-dark:#c94f12;
  --blue:#1a8fd6;
  --ink:#222;
  --grey:#9a9a9a;
  --light:#e9e9e9;
  --footer:#2e2e2e;
  --white:#fff;
}
*{margin:0;padding:0;box-sizing:border-box}
html,body{width:896px;height:1200px;overflow:hidden;background:var(--white)}
body{position:relative;font-family:"Open Sans",sans-serif;color:var(--ink)}
.header{position:absolute;left:0;top:0;width:896px;height:67px}
.brand{position:absolute;left:62px;top:20px;display:flex;align-items:center;gap:8px;font-family:"Questrial",sans-serif;font-size:19px;color:var(--orange);white-space:nowrap}
.brand-mark{width:18px;height:18px;background:var(--orange)}
.divider{position:absolute;left:297px;top:16px;width:1px;height:35px;background:var(--light)}
.change-site{position:absolute;left:308px;top:29px;font-size:8px;color:#b5b5b5;display:flex;align-items:center;gap:4px;white-space:nowrap}
.change-site i{width:10px;height:10px;border:1px solid #ccc;border-radius:50%}
.social{position:absolute;display:flex;gap:7px}
.header .social{left:631px;top:30px}
.social span{width:16px;height:16px;transform:rotate(45deg);background:#d4d4d4}
.social span.on{background:var(--blue)}
.search{position:absolute;left:734px;top:29px;width:100px;height:18px;border-radius:9px;background:var(--light);font-size:8px;color:#aaa;padding:4px 7px}
.search svg{position:absolute;right:7px;top:4px}
.nav{position:absolute;left:0;top:67px;width:896px;height:35px;background:var(--orange)}
.nav-list{position:absolute;left:62px;top:0;width:772px;height:35px;display:flex;align-items:center;justify-content:space-between;font-family:"Questrial",sans-serif;font-size:9.4px;color:var(--white);text-transform:uppercase;white-space:nowrap}
.nav-list span{white-space:nowrap}
.nav-list .active{color:#222}
.hero{position:absolute;left:0;top:102px;width:896px;height:344px;background:linear-gradient(180deg,#8c8a8e 0%,#b7a598 45%,#8a7a70 70%,#6d6260 100%)}
.dropdown{position:absolute;left:139px;top:102px;width:140px;height:130px;background:var(--white);padding:18px 0 0 18px;font-size:9.5px;line-height:20px;white-space:nowrap}
.dropdown .first{border-bottom:1px solid #eee}
.hero-title{position:absolute;left:137px;top:255px;font-family:"Fjalla One",sans-serif;font-weight:400;font-size:40px;color:var(--white);letter-spacing:-.5px;white-space:nowrap;text-shadow:0 1px 3px rgba(0,0,0,.4)}
.hero-sub{position:absolute;left:141px;top:304px;font-size:19px;color:var(--white);white-space:nowrap;text-shadow:0 1px 3px rgba(0,0,0,.5)}
.cta{position:absolute;left:140px;top:345px}
.cta span{position:absolute;left:11px;top:8px;font-family:"Questrial",sans-serif;font-size:15px;color:var(--white);white-space:nowrap}
.dots{position:absolute;left:138px;top:395px;display:flex;gap:2px}
.dots i{width:22px;height:4px;background:rgba(255,255,255,.5)}
.dots i.on{background:var(--orange)}
.thumbs{position:absolute;left:696px;top:266px;width:59px;height:180px;background:var(--white);padding:6px 4px}
.thumbs div{width:48px;height:45px;margin-bottom:5px;background:linear-gradient(#9aa4ae,#7d746e)}
.thumbs div.on{outline:2px solid var(--blue)}
.thumbs p{font-size:9px;color:var(--orange);text-align:center}
.who{position:absolute;left:325px;top:480px;width:250px;font-family:"Montserrat",sans-serif;font-weight:700;font-size:34px;line-height:44px;color:var(--blue);letter-spacing:-1px;white-space:nowrap}
.intro{position:absolute;left:208px;top:534px;width:480px;text-align:center;font-size:9.2px;line-height:11px}
.connector{position:absolute;left:0;top:0}
.gallery-title{position:absolute;left:0;top:680px;width:896px;text-align:center;font-family:"Questrial",sans-serif;font-weight:400;font-size:18px;white-space:nowrap}
.gallery{position:absolute;left:0;top:723px;width:896px;display:grid;grid-template-columns:repeat(4,222px);grid-auto-rows:207px;gap:2px}
.tile{background:linear-gradient(#a9b4bd,#8e7a68)}
.tile.sky{background:linear-gradient(#c9d3dc,#9a8468)}
.tile.roofs{background:linear-gradient(#b89b82,#8c7563)}
.tile.green{background:linear-gradient(#9a8a7c,#5e7a44)}
.tile.tower{background:linear-gradient(#c7cfd2 60%,#c6b545)}
.feature{background:var(--orange);position:relative;color:var(--white);text-align:center}
.feature .frame{position:absolute;inset:15px;border:1px solid var(--orange-dark)}
.feature h3{position:absolute;left:0;right:0;top:63px;font-weight:400;font-size:14px;white-space:nowrap}
.feature p{position:absolute;left:40px;right:40px;top:89px;font-size:9px;line-height:11px}
.feature svg{position:absolute;left:86px;top:122px}
.footer{position:absolute;left:0;top:1141px;width:896px;height:59px;background:var(--footer);overflow:hidden}
.footer .backdrop{position:absolute;left:-10px;top:-14px;font-family:"Fjalla One",sans-serif;font-size:110px;color:#3a3a3a;white-space:nowrap}
.footer nav{position:absolute;left:139px;top:26px;font-size:8px;color:var(--white);display:flex;gap:6px;white-space:nowrap}
.footer nav .copy{margin-left:12px}
.footer .social{left:671px;top:23px}
.footer .social span{background:#bbb}
.footer .social span.on{background:var(--blue)}
</style>
</head>
<body>
<header class="header">
  <div class="brand"><span class="brand-mark"></span>Leopold-Kolbrand-Haus</div>
  <div class="divider"></div>
  <div class="change-site"><i></i>Change Site</div>
  <div class="social"><span></span><span class="on"></span><span></span><span></span></div>
  <div class="search">Search
    <svg width="9" height="9" viewBox="0 0 9 9"><circle cx="3.6" cy="3.6" r="2.6" fill="none" stroke="#fff" stroke-width="1.3"/><line x1="5.5" y1="5.5" x2="8.3" y2="8.3" stroke="#fff" stroke-width="1.3"/></svg>
  </div>
</header>

<nav class="nav">
  <div class="nav-list">
    <span>Home</span><span>Stadt Wendau</span><span class="active">Das Haus</span><span>Wohnungen</span><span>Wohnqualität</span><span>Büros</span><span>Klimaanlagen</span><span>Gewerbl. Mieter</span><span>Links / Anfahrt</span><span>Kontakt</span><span>Impressum</span><span>Vermietung</span>
  </div>
</nav>

<section class="hero" role="img" aria-label="Marktplatz mit Marktständen vor historischen Häuserfassaden"></section>
<div class="dropdown">
  <div class="first">Standort / Gebäude</div>
  <div>Eingänge</div><div>Treppenhäuser</div><div>Dachterrasse</div><div>Terrassenausstattung</div>
</div>
<h1 class="hero-title">LOREM IPSUM TEXT</h1>
<p class="hero-sub">Amet donor lorem ipsum sit text</p>
<div class="cta">
  <svg width="133" height="34" viewBox="0 0 133 34"><path d="M0 0H133L120 17L133 34H0Z" fill="#1a8fd6"/></svg>
  <span>Call to Action</span>
</div>
<div class="dots"><i class="on"></i><i></i><i></i></div>
<aside class="thumbs">
  <div class="on" role="img" aria-label="Marktstände"></div>
  <div role="img" aria-label="Innenraum"></div>
  <div role="img" aria-label="Stadtansicht"></div>
  <p>View All</p>
</aside>

<svg class="connector" width="896" height="700" viewBox="0 0 896 700">
  <g fill="none" stroke="#777" stroke-width="0.8">
    <polyline points="311,505 164,505 164,603 448,603 448,677"/>
    <polyline points="311,501 304,505 311,509"/>
    <polyline points="444,670 448,678 452,670"/>
  </g>
</svg>
<h2 class="who">WHO WE ARE</h2>
<p class="intro">Lorem ipsum dolor sit amet, consectetur adipiscing elit. In fermentum dolor non augue pretium egestas. Donec sem eros, tincidunt at congue ut, posuere sit amet est. Vivamus scelerisque viverra odio sit amet laoreet. Ut nec neque non justo rutrum tempor lobortis eu ante.</p>
<h2 class="gallery-title">Gallery or Lorem Ipsum Heading</h2>

<section class="gallery">
  <div class="tile sky" role="img" aria-label="Fassade des Hauses am Markt"></div>
  <div class="feature">
    <div class="frame"></div>
    <h3>Lorem Ipsum Text</h3>
    <p>Ut nec neque non justo rutrum tempor lobortis eu ante.</p>
    <svg width="46" height="46" viewBox="0 0 46 46"><circle cx="23" cy="23" r="21" fill="none" stroke="#fff" stroke-width="2"/><path d="M23 15V31M15 23H31" stroke="#fff" stroke-width="2"/></svg>
  </div>
  <div class="tile sky" role="img" aria-label="Rathaus mit Turm am Marktplatz"></div>
  <div class="tile roofs" role="img" aria-label="Luftbild der Altstadt"></div>
  <div class="tile green" role="img" aria-label="Blick über die Dächer der Stadt"></div>
  <div class="tile" role="img" aria-label="Historisches Rathaus"></div>
  <div class="tile" role="img" aria-label="Häuserzeile am Markt"></div>
  <div class="tile tower" role="img" aria-label="Kirchturm mit Uhr"></div>
</section>

<footer class="footer">
  <div class="backdrop">nd-Kolbran</div>
  <nav><span>Home</span><span>About Us</span><span>Gallery</span><span>Contact us</span><span class="copy">© 2014 Terms and Policy</span></nav>
  <div class="social"><span></span><span class="on"></span><span></span><span></span></div>
</footer>
</body>
</html>
```